Thankyou Card

- Thank you cards for my buyers
We are an online women's fashion boutique, we are after a thank you card that will be distributed after purchase
ideally on the card it will have logo - Website - Slogan- A thank you message
The card will be Bright, Fun & Inviting wanting the customer to return to our site
Attached it a copy of our logo web page and slogan -

Website - quenzel.com.au

Fashion

• Business Name - Quenzel
Web Address - www.quenzel.com.au
Thank you for your purchase note
Slogan - Live, Laugh, Love & Shop...

```html
<!DOCTYPE html>
<html lang="en">
<head>
<meta charset="utf-8">
<title>Quenzel – Thank You Card</title>
<link rel="stylesheet" href="https://fonts.googleapis.com/css2?family=Lato:ital,wght@0,700;0,900;1,700&display=swap">
<style>
  :root {
    --backdrop: #3a3a3a;
    --card: #f9f9f9;
    --ink: #0d0d0d;
    --accent: #c8174a;
    --band: #000000;
  }
  * { margin: 0; padding: 0; box-sizing: border-box; }
  html, body {
    width: 1200px;
    height: 750px;
    overflow: hidden;
    background: var(--backdrop);
    font-family: "Lato", Arial, sans-serif;
    color: var(--ink);
  }
  .canvas {
    position: relative;
    width: 1200px;
    height: 750px;
  }
  .card {
    position: absolute;
    top: 207px;
    width: 542px;
    height: 310px;
    background: var(--card);
    border-radius: 19px;
    overflow: hidden;
  }
  .card--front { left: 44px; }
  .card--back { left: 614px; }

  .brand-name {
    position: absolute;
    font-weight: 900;
    color: var(--ink);
    letter-spacing: -0.5px;
    line-height: 1;
    white-space: nowrap;
  }
  .brand-dot {
    display: inline-block;
    background: var(--accent);
    border-radius: 50%;
  }

  /* front */
  .card--front .brand-name {
    right: 288px;
    top: 120px;
    font-size: 42px;
  }
  .card--front .brand-dot {
    width: 9px; height: 9px;
    margin-left: 3px;
  }
  .slogan {
    position: absolute;
    right: 287px;
    top: 170px;
    font-size: 15.5px;
    font-weight: 700;
    font-style: italic;
    white-space: nowrap;
  }
  .slogan .hl, .web-address .hl { color: var(--accent); }
  .divider {
    position: absolute;
    left: 276px;
    top: 102px;
    width: 2px;
    height: 106px;
    background: linear-gradient(to bottom, transparent, var(--ink) 15%, var(--ink) 85%, transparent);
  }
  .web-address {
    position: absolute;
    left: 294px;
    top: 144px;
    font-size: 16.5px;
    font-weight: 900;
    white-space: nowrap;
  }
  .rule {
    position: absolute;
    left: 0; right: 0;
    top: 279px;
    height: 1.5px;
    background: var(--accent);
  }
  .band {
    position: absolute;
    left: 0; right: 0;
    top: 282px;
    bottom: 0;
    background: var(--band);
  }

  /* back */
  .card--back .brand-name {
    left: 0; right: 0;
    top: 132px;
    text-align: center;
    font-size: 48px;
  }
  .card--back .brand-dot {
    width: 10px; height: 10px;
    margin-left: 4px;
  }
  .thanks {
    position: absolute;
    left: 0; right: 0;
    top: 247px;
    text-align: center;
    font-size: 17px;
    font-weight: 900;
  }
</style>
</head>
<body>
<main class="canvas">
  <section class="card card--front" aria-label="Card front">
    <div class="brand-name">Quenzel<span class="brand-dot"></span></div>
    <p class="slogan">Live, <span class="hl">Laugh</span>, Love &amp; <span class="hl">Shop...</span></p>
    <div class="divider"></div>
    <p class="web-address">www.<span class="hl">quenzel</span>.com.au</p>
    <div class="rule"></div>
    <div class="band"></div>
  </section>

  <section class="card card--back" aria-label="Card back">
    <div class="brand-name">Quenzel<span class="brand-dot"></span></div>
    <p class="thanks">Thank you for your purchase</p>
  </section>
</main>
</body>
</html>
```